Business card design for Velvet Harbor

We need business cards designed for our new marketing consulting company, Velvet Harbor. Our services include marketing strategy, go-to-market and launch planning, growth strategy, and execution. We serve medical technology and health technology companies, from startups to well-established growth companies.

The business cards should feel professional, credible, reliable and trustworthy, and should instill confidence. Also bold, creative, and modern.

The design must use the Velvet Harbor logo.

The primary brand color is this orange: #FF5501
A secondary color that you can use is this gray: #282B2D
I would prefer only to use the orange and gray. But if you feel you really need an additional accent color (please use it very sparingly, as little as possible), you can use this blue for small accent purposes: #009FED

Attached are the logo files. The main logo is the one with a little bit of orange on the left and the rest is gray.

The business card should include the following:

Velvet Harbor logo
First name and last name
Title
Email address
Phone number and type (in whatever order looks best for the design
Website (the website does not need to be in the same block as the personal info)

For example:

Nessa Pryle
Founder & Principal
nessa@velvetharbor.com
+1.628.309.4156 mobile (can use "." or spaces in between blocks of numbers)
velvetharbor.com (somewhere on the card, it does not need to be with the personal info; and note that there is no "www." at the beginning)

Note that there will be no address listed on the business card.

Target Market(s)

Executives (CEO, head of marketing, head of sales) at medical technology and health technology companies, mostly in their 40s and older, well-educated, often with advanced degrees. They are strategic thinkers, responsible for budgets, and familiar with P&L. Their comfort with and trust in using outside consultants varies.

Industry/Entity Type

Medical technology and health technology companies.

Contact Information for Business Card

See project description

Font styles to use
Sans Serif

Requirements
Must have
• Logo and see Business card details section above.

```html
<!DOCTYPE html>
<html lang="en">
<head>
<meta charset="utf-8">
<title>Velvet Harbor — Business Card</title>
<link rel="stylesheet" href="https://fonts.googleapis.com/css2?family=Montserrat:wght@400;700;800&display=swap">
<style>
  :root {
    --orange: #FF5501;
    --orange-print: #F05A22;
    --gray: #282B2D;
    --gray-soft: #313537;
    --symbol-area: #E6E7E8;
    --white: #FFFFFF;
    --ink: #2A2C2E;
    --stage: #1A1B1C;
  }
  * { box-sizing: border-box; margin: 0; padding: 0; }
  html, body {
    width: 1200px; height: 1200px; overflow: hidden;
    background: var(--stage);
    font-family: "Montserrat", sans-serif;
  }
  .canvas {
    position: relative; width: 1200px; height: 1200px;
    display: flex; align-items: center; justify-content: center; gap: 60px;
  }
  .card {
    position: relative; width: 420px; height: 720px;
    border-radius: 26px; overflow: hidden;
  }

  /* Front */
  .card-front { background: var(--white); }
  .front-shape { position: absolute; inset: 0; width: 100%; height: 100%; }
  .brand-name {
    font-family: "Montserrat", sans-serif; font-weight: 700;
    color: var(--white); line-height: 1.1;
  }
  .front-brand {
    position: absolute; top: 40px; left: 0; right: 0; text-align: center;
    font-size: 44px;
  }
  .symbol-area {
    position: absolute; border-radius: 50%;
  }
  .front-symbol {
    left: 78px; top: 186px; width: 264px; height: 264px;
    background: var(--symbol-area);
  }
  .person {
    position: absolute; top: 484px; left: 0; right: 0; text-align: center;
  }
  .person-name {
    color: var(--orange-print); font-weight: 800; font-size: 34px;
    letter-spacing: 1px; text-transform: uppercase; line-height: 1.15;
  }
  .person-title {
    color: var(--ink); font-weight: 400; font-size: 16px; margin-top: 2px;
  }
  .contact-divider {
    position: absolute; top: 584px; left: 40px; right: 40px;
    display: flex; align-items: center; gap: 8px;
  }
  .contact-divider .rule { flex: 1; height: 1.5px; background: var(--orange-print); }
  .contact-icon {
    width: 26px; height: 26px; border-radius: 50%;
    background: var(--orange-print);
    display: flex; align-items: center; justify-content: center;
  }
  .contact-icon svg { width: 14px; height: 14px; }
  .contact-list {
    position: absolute; top: 622px; left: 0; right: 0; text-align: center;
    list-style: none; color: var(--ink); font-size: 15px; line-height: 1.5;
  }
  .front-band {
    position: absolute; left: 0; right: 0; bottom: 0; height: 14px;
    background: var(--orange-print);
  }

  /* Back */
  .card-back { background: var(--gray); }
  .back-symbol {
    left: 30px; top: 140px; width: 360px; height: 360px;
    background: var(--gray-soft);
  }
  .back-lockup {
    position: absolute; left: 0; right: 0; top: 296px;
    display: flex; align-items: center; justify-content: center; gap: 14px;
  }
  .back-dot { width: 30px; height: 30px; border-radius: 50%; background: var(--orange); flex: none; }
  .back-brand { font-size: 32px; }
</style>
</head>
<body>
<main class="canvas">
  <section class="card card-front" aria-label="Business card front">
    <svg class="front-shape" viewBox="0 0 420 720" preserveAspectRatio="none" aria-hidden="true">
      <path d="M0 0 H420 V392 Q210 520 0 232 Z" fill="var(--gray)"/>
      <path d="M0 246 Q210 548 420 404" fill="none" stroke="var(--orange-print)" stroke-width="4"/>
    </svg>
    <h1 class="brand-name front-brand">Velvet Harbor</h1>
    <div class="symbol-area front-symbol" role="img" aria-label="Large brand symbol"></div>

    <div class="person">
      <p class="person-name">Nessa Pryle</p>
      <p class="person-title">Founder &amp; Principal</p>
    </div>

    <div class="contact-divider" aria-hidden="true">
      <span class="rule"></span>
      <span class="contact-icon">
        <svg viewBox="0 0 24 24"><path fill="#fff" d="M6.6 10.8a15.1 15.1 0 0 0 6.6 6.6l2.2-2.2c.3-.3.7-.4 1-.2 1.1.4 2.3.6 3.6.6.6 0 1 .4 1 1V20c0 .6-.4 1-1 1A17 17 0 0 1 3 4c0-.6.4-1 1-1h3.5c.6 0 1 .4 1 1 0 1.3.2 2.5.6 3.6.1.3 0 .7-.2 1z"/></svg>
      </span>
      <span class="contact-icon">
        <svg viewBox="0 0 24 24"><rect x="3" y="6" width="18" height="12" rx="1" fill="#fff"/><path d="M3 6l9 7 9-7" fill="none" stroke="var(--orange-print)" stroke-width="1.6"/></svg>
      </span>
      <span class="contact-icon">
        <svg viewBox="0 0 24 24" fill="none" stroke="#fff" stroke-width="1.8"><circle cx="12" cy="12" r="9"/><ellipse cx="12" cy="12" rx="4" ry="9"/><path d="M3 12h18"/></svg>
      </span>
      <span class="rule"></span>
    </div>

    <ul class="contact-list">
      <li>+1.628.309.4156</li>
      <li>nessa@velvetharbor.com</li>
      <li>velvetharbor.com</li>
    </ul>
    <div class="front-band"></div>
  </section>

  <section class="card card-back" aria-label="Business card back">
    <div class="symbol-area back-symbol" role="img" aria-label="Faint large brand symbol"></div>
    <div class="back-lockup">
      <span class="back-dot" aria-hidden="true"></span>
      <p class="brand-name back-brand">Velvet Harbor</p>
    </div>
  </section>
</main>
</body>
</html>
```